Brisk Harbor Funding - Letterhead

We need letterhead options for our case funding company called Brisk Harbor Funding. Here are some of the details:

Name - Brisk Harbor Funding
Phone - (555) 214 - 9083
Address - 38 Larkmoor Avenue
Suite 412
New York, NY 10958
Website - briskharborfunding.example

```html
<!DOCTYPE html>
<html lang="en">
<head>
<meta charset="utf-8">
<title>Brisk Harbor Funding – Letterhead</title>
<link rel="stylesheet" href="https://fonts.googleapis.com/css2?family=Questrial&family=Roboto:wght@400&display=swap">
<style>
  :root {
    --backdrop: #5b7890;
    --paper: #ecebee;
    --navy: #0d2444;
    --slate: #53697a;
    --steel: #7a8a96;
    --ink-contact: #3b4a5c;
    --ink-body: #4a4c52;
    --brand: #1a3050;
  }
  * { box-sizing: border-box; margin: 0; padding: 0; }
  html, body {
    width: 1200px; height: 1013px; overflow: hidden;
    background: var(--backdrop);
  }
  .letterhead {
    position: absolute;
    left: 267px; top: 36px;
    width: 666px; height: 940px;
    background: var(--paper);
    font-family: "Roboto", sans-serif;
  }
  .brand {
    position: absolute; left: 52px; top: 92px;
    display: flex; align-items: center; gap: 10px;
    font-family: "Questrial", sans-serif;
    font-size: 17px; line-height: 1.05;
    letter-spacing: 1.5px; text-transform: uppercase;
    color: var(--brand);
  }
  .brand-square { width: 44px; height: 44px; background: var(--brand); flex: none; }
  .contact {
    position: absolute; right: 40px; top: 97px;
    text-align: right;
    font-family: "Questrial", sans-serif;
    font-size: 13.5px; line-height: 15.5px;
    color: var(--ink-contact);
  }
  .contact .address { margin-top: 11px; }
  .salutation, .signoff {
    position: absolute;
    font-family: "Questrial", sans-serif;
    font-size: 12px; color: var(--ink-body);
  }
  .salutation { left: 42px; top: 250px; }
  .signoff { right: 50px; top: 814px; }
  .body-copy {
    position: absolute; left: 42px; right: 41px; top: 324px;
    font-size: 10.6px; line-height: 13.6px;
    color: var(--ink-body); text-align: justify;
  }
  .body-copy p + p { margin-top: 13.6px; }
  .footer-band {
    position: absolute; left: 0; right: 0; bottom: 0; height: 21px;
    display: flex; gap: 4px;
  }
  .footer-band span { flex: 1; }
  .band-navy { background: var(--navy); }
  .band-slate { background: var(--slate); }
  .band-steel { background: var(--steel); }
</style>
</head>
<body>
<main class="letterhead">
  <div class="brand">
    <span class="brand-square"></span>
    <span class="brand-name">Brisk<br>Harbor<br>Funding</span>
  </div>

  <address class="contact" style="font-style:normal">
    <div>(555) 214 - 9083</div>
    <div>briskharborfunding.example</div>
    <div class="address">38 Larkmoor Avenue<br>Suite 412, New York, NY 10958</div>
  </address>

  <p class="salutation">Lorem ipsum</p>

  <section class="body-copy">
    <p>Lorem ipsum dolor sit amet, consectetur adipiscing elit. In fringilla malesuada dolor sit amet molestie. Aliquam facilisis tincidunt justo vitae ullamcorper. Duis eu lacus nec ex maximus scelerisque vel ac nulla. Fusce nec blandit eros. Nam volutpat est id rhoncus faucibus. Nunc eget egestas mi. Fusce in pharetra lorem, et laoreet diam. Proin aliquet urna et accumsan interdum. Proin egestas dapibus nibh, a vestibulum dui molestie vitae. Fusce ac massa sed quam posuere euismod.</p>
    <p>Ut vel gravida ante, nec mattis metus. Nulla facilisi. Aenean maximus eu eros in tempor. Sed in sapien tincidunt purus accumsan lacinia. Praesent iaculis metus laoreet purus eleifend malesuada. Nam sit amet nisl maximus, porta nunc vitae, venenatis nibh. Aliquam tempor quam vitae metus semper, at egestas mauris condimentum. Integer placerat pharetra erat vitae imperdiet. Aliquam felis ante, pellentesque ac lacinia nec, varius ac eros. Maecenas finibus neque egestas, ornare sapien id, ullamcorper odio. Aliquam tempus congue magna, vel facilisis mi dapibus at. Nullam magna lorem, auctor eget gravida eu, congue tincidunt urna. Sed varius laoreet urna vel elementum.</p>
    <p>Fusce et finibus erat, non lobortis urna. Proin sed risus dui. Cras molestie, nisi et elementum ornare, odio justo condimentum tellus, vel eleifend augue eros a lacus. Proin varius suscipit sem at blandit. Vestibulum placerat nunc molestie augue feugiat egestas. Donec lorem velit, pharetra quis euismod vitae, egestas eget mi. Ut vestibulum sapien eget hendrerit condimentum. Vestibulum viverra, arcu sed vulputate sodales, tortor ligula commodo diam, a luctus nibh eros ac augue. Aliquam commodo ultrices est at interdum. Vestibulum non malesuada dui. Maecenas ullamcorper risus nunc, et elementum enim volutpat vel. Pellentesque enim urna, bibendum et neque eu, sollicitudin laoreet ipsum. Fusce a eros enim.</p>
    <p>Nunc at est finibus nunc semper pretium. Aenean vestibulum sit amet libero ac dapibus. Proin sed aliquet tellus. Nunc elit libero, dapibus eu massa nec, ullamcorper commodo metus. Pellentesque rutrum quam at posuere congue. Suspendisse accumsan ultrices erat sit amet convallis. Curabitur a eleifend lacus. Sed sit amet porttitor enim, et rhoncus urna. Praesent non cursus dolor. Maecenas libero lectus, tincidunt a molestie ac, pellentesque eget tellus. Suspendisse consectetur nisl sed neque accumsan semper. Praesent in luctus tortor. Duis porta, orci quis ultrices congue, lorem est euismod dui, non accumsan tortor est vitae felis. Phasellus cursus purus ac rhoncus convallis.</p>
    <p>Mauris sodales urna dapibus ligula condimentum blandit. Nulla nec tempor lorem. Aenean tempus odio ac justo mattis, et ultricies ante congue. Nunc eget risus nec leo fermentum volutpat a id mauris. Nunc aliquam efficitur felis, a imperdiet ante mollis at. Cras quis finibus nunc. Mauris dapibus cursus sapien, egestas egestas lacus laoreet ac. Nullam dolor nibh, feugiat at leo ac, porta consectetur sem. Nullam et purus dui.</p>
  </section>

  <p class="signoff">Lorem ipsum</p>

  <div class="footer-band">
    <span class="band-navy"></span>
    <span class="band-slate"></span>
    <span class="band-steel"></span>
  </div>
</main>
</body>
</html>
```